MSA Plans

I would like to rebuild my brochure for the 3 business plans that I currently offer my clients. I would like to make it look much more modern & attractive to clients when choosing one of our service plans. If we can stick to a tech theme that would be great. Message me for anymore information.

```html
<!DOCTYPE html>
<html lang="en">
<head>
<meta charset="utf-8">
<title>MSA Plans</title>
<link href="https://fonts.googleapis.com/css2?family=Montserrat:wght@400;500;600;700&display=swap" rel="stylesheet">
<style>
:root{
  --orange:#ee7232;
  --peach:#fde3d6;
  --grey:#f2f2f3;
  --ink:#0b0b0b;
  --white:#ffffff;
  --green:#3fa34d;
  --red:#e0262b;
  --text:#1d1d1d;
}
*{margin:0;padding:0;box-sizing:border-box}
html,body{width:1200px;height:881px;overflow:hidden}
body{background:var(--orange);font-family:'Montserrat',sans-serif;color:var(--text);position:relative}
.page{position:absolute;top:88px;width:498px;height:705px;background:var(--white)}
.page--msa{left:79px}
.page--cyber{left:623px}
.plan-table{position:absolute;left:17.5px;top:29px;width:463px}
.table-head{display:grid;height:24px;background:var(--ink);color:var(--white);font-size:9.6px;font-weight:500;align-items:center}
.table-head span{text-align:center}
.table-head .title{text-align:left;padding-left:10px}
.msa .table-head,.msa .row{grid-template-columns:230px repeat(3,1fr);column-gap:2px}
.cyber .table-head,.cyber .row{grid-template-columns:307px repeat(2,1fr);column-gap:2px}
.section-bar{height:17px;margin-top:2px;background:var(--orange);color:var(--white);font-size:9.4px;font-weight:500;padding-left:10px;line-height:17px}
.row{display:grid;height:18.3px;margin-top:2px;font-size:8.6px}
.row .label{background:var(--peach);padding-left:10px;display:flex;align-items:center;white-space:nowrap}
.row .label small{font-size:6.4px;margin-left:3px}
.row .cell{background:var(--grey);display:flex;align-items:center;justify-content:center;text-align:center;line-height:1}
.row--tall{height:23px}
.cyber .row:first-of-type{margin-top:3px}
.icon{width:13px;height:13px}
.price-block{background:var(--ink);padding:7px 0 5px;margin-top:2px}
.price-line{display:grid;height:16px;align-items:center;font-size:8.8px;font-weight:600}
.msa .price-line{grid-template-columns:230px repeat(3,1fr);column-gap:2px}
.cyber .price-line{grid-template-columns:1fr 76px 76px 76px;column-gap:2px}
.price-line .name{color:var(--orange);padding-left:10px}
.price-line .val{color:var(--white);text-align:center;font-weight:500}
.cyber .price-block{margin-top:8px}
.footer{position:absolute;left:17.5px;top:620px;width:463px;height:55px;background:var(--orange);color:var(--white);text-align:center;padding-top:9px}
.footer .company{font-size:10.4px;font-weight:600;margin-bottom:3px}
.footer .contact{font-size:8.4px;font-weight:500;line-height:10.5px}
.brand{position:absolute;left:144px;top:575px;display:flex;align-items:center;gap:9px}
.brand .dot{width:22px;height:22px;border-radius:50%;background:var(--orange)}
.brand .name{font-size:22px;font-weight:600;color:var(--ink);letter-spacing:1.5px}
</style>
</head>
<body>
<svg width="0" height="0" style="position:absolute" aria-hidden="true">
  <symbol id="tick" viewBox="0 0 20 20">
    <circle cx="9.5" cy="11" r="7.5" fill="none" stroke="#3fa34d" stroke-width="1.8"/>
    <path d="M5.5 10.5 L9 14.5 L17 2.5" fill="none" stroke="#3fa34d" stroke-width="2.4" stroke-linecap="round" stroke-linejoin="round"/>
  </symbol>
  <symbol id="cross" viewBox="0 0 20 20">
    <circle cx="10" cy="10.5" r="7.5" fill="none" stroke="#e0262b" stroke-width="1.8"/>
    <path d="M6.5 6.5 L13.5 14.5 M14 6 L6.5 14.5" fill="none" stroke="#e0262b" stroke-width="2.2" stroke-linecap="round"/>
  </symbol>
</svg>

<section class="page page--msa">
  <div class="plan-table msa">
    <div class="table-head"><span class="title">Managed Services Agreement</span><span>Essential</span><span>Business</span><span>Professional</span></div>

    <div class="section-bar">Support</div>
    <div class="row"><div class="label">Unlimited Remote Support 7am to 6pm</div><div class="cell"><svg class="icon"><use href="#tick"/></svg></div><div class="cell"><svg class="icon"><use href="#tick"/></svg></div><div class="cell"><svg class="icon"><use href="#tick"/></svg></div></div>
    <div class="row"><div class="label">3rd Party Vendor Support</div><div class="cell"><svg class="icon"><use href="#tick"/></svg></div><div class="cell"><svg class="icon"><use href="#tick"/></svg></div><div class="cell"><svg class="icon"><use href="#tick"/></svg></div></div>
    <div class="row"><div class="label">Reactive Onsite Support 8am to 5pm</div><div class="cell">VIP Rates</div><div class="cell"></div><div class="cell"><svg class="icon"><use href="#tick"/></svg></div></div>
    <div class="row"><div class="label">After-Hours Support</div><div class="cell">VIP Rates</div><div class="cell">VIP Rates</div><div class="cell"><svg class="icon"><use href="#tick"/></svg></div></div>

    <div class="section-bar">Service</div>
    <div class="row"><div class="label">Guaranteed SLA Response Times</div><div class="cell"><svg class="icon"><use href="#tick"/></svg></div><div class="cell"><svg class="icon"><use href="#tick"/></svg></div><div class="cell"><svg class="icon"><use href="#tick"/></svg></div></div>
    <div class="row"><div class="label">24x7 Website &amp; Infrastructure Monitoring</div><div class="cell"><svg class="icon"><use href="#tick"/></svg></div><div class="cell"><svg class="icon"><use href="#tick"/></svg></div><div class="cell"><svg class="icon"><use href="#tick"/></svg></div></div>
    <div class="row"><div class="label">Secure Web Content Filtering</div><div class="cell"><svg class="icon"><use href="#tick"/></svg></div><div class="cell"><svg class="icon"><use href="#tick"/></svg></div><div class="cell"><svg class="icon"><use href="#tick"/></svg></div></div>
    <div class="row"><div class="label">Backup Monitoring</div><div class="cell"><svg class="icon"><use href="#tick"/></svg></div><div class="cell"><svg class="icon"><use href="#tick"/></svg></div><div class="cell"><svg class="icon"><use href="#tick"/></svg></div></div>
    <div class="row"><div class="label">Workstation OS Patching &amp; Updating</div><div class="cell"><svg class="icon"><use href="#tick"/></svg></div><div class="cell"><svg class="icon"><use href="#tick"/></svg></div><div class="cell"><svg class="icon"><use href="#tick"/></svg></div></div>
    <div class="row"><div class="label">CEO / MD Home Tech Support</div><div class="cell"><svg class="icon"><use href="#tick"/></svg></div><div class="cell"><svg class="icon"><use href="#tick"/></svg></div><div class="cell"><svg class="icon"><use href="#tick"/></svg></div></div>
    <div class="row"><div class="label">Monthly Tech Site Visit</div><div class="cell"><svg class="icon"><use href="#cross"/></svg></div><div class="cell">Quarterly</div><div class="cell">Monthly</div></div>
    <div class="row"><div class="label">Short Term Loan Equipment</div><div class="cell"><svg class="icon"><use href="#cross"/></svg></div><div class="cell">1 Month</div><div class="cell">3 Months</div></div>
    <div class="row"><div class="label">Adds / Moves / Changes (Staff)</div><div class="cell"><svg class="icon"><use href="#tick"/></svg></div><div class="cell"><svg class="icon"><use href="#tick"/></svg></div><div class="cell"><svg class="icon"><use href="#tick"/></svg></div></div>
    <div class="row"><div class="label">Adds / Moves / Changes (Workstations)</div><div class="cell">VIP Rates</div><div class="cell">VIP Rates</div><div class="cell"><svg class="icon"><use href="#tick"/></svg></div></div>

    <div class="section-bar">Management</div>
    <div class="row"><div class="label">Asset and Warranty Tracking &amp; Reporting</div><div class="cell"><svg class="icon"><use href="#tick"/></svg></div><div class="cell"><svg class="icon"><use href="#tick"/></svg></div><div class="cell"><svg class="icon"><use href="#tick"/></svg></div></div>
    <div class="row"><div class="label">Comprehensive IT Documentation</div><div class="cell"><svg class="icon"><use href="#tick"/></svg></div><div class="cell"><svg class="icon"><use href="#tick"/></svg></div><div class="cell"><svg class="icon"><use href="#tick"/></svg></div></div>
    <div class="row"><div class="label">Technology Strategy Meeting</div><div class="cell">Annual</div><div class="cell">Quarterly</div><div class="cell">Monthly</div></div>
    <div class="row"><div class="label">Technology Business Review Meeting</div><div class="cell">Annual</div><div class="cell">Bi Annual</div><div class="cell">Quarterly</div></div>
    <div class="row"><div class="label">IT Policy Templates</div><div class="cell"><svg class="icon"><use href="#cross"/></svg></div><div class="cell"><svg class="icon"><use href="#tick"/></svg></div><div class="cell"><svg class="icon"><use href="#tick"/></svg></div></div>

    <div class="section-bar">Training</div>
    <div class="row"><div class="label">End User Training Materials</div><div class="cell"><svg class="icon"><use href="#cross"/></svg></div><div class="cell"><svg class="icon"><use href="#cross"/></svg></div><div class="cell"><svg class="icon"><use href="#tick"/></svg></div></div>
    <div class="row"><div class="label">Security Awareness Training</div><div class="cell"><svg class="icon"><use href="#tick"/></svg></div><div class="cell"><svg class="icon"><use href="#tick"/></svg></div><div class="cell"><svg class="icon"><use href="#tick"/></svg></div></div>

    <div class="price-block">
      <div class="price-line"><span class="name">RRP / User</span><span class="val">$110</span><span class="val">$130</span><span class="val">$165</span></div>
      <div class="price-line"><span class="name">Minimum User Count</span><span class="val">5</span><span class="val">5</span><span class="val">5</span></div>
      <div class="price-line"><span class="name">Minimum Monthly Commit</span><span class="val">$550</span><span class="val">$650</span><span class="val">$825</span></div>
    </div>
  </div>

  <footer class="footer">
    <p class="company">NORTHGATE COMPUTER SERVICES PTY LTD | ABN: 51 208 334 917</p>
    <p class="contact">northgatecomputers.com.au | service@northgatecomputers.com.au<br>12/48 Ashby Rd, Riverside Park, VIC, 3099 | 1300 555 019</p>
  </footer>
</section>

<section class="page page--cyber">
  <div class="plan-table cyber">
    <div class="table-head"><span class="title">Cybersecurity Packages</span><span>Business</span><span>Professional</span></div>

    <div class="row"><div class="label">Compliance with ACSC Essential 8 Maturity</div><div class="cell"><svg class="icon"><use href="#tick"/></svg></div><div class="cell"><svg class="icon"><use href="#tick"/></svg></div></div>
    <div class="row"><div class="label">Security Standard -<small>Alignment to Northgate Cloud Office Security Policy &amp; Reporting</small></div><div class="cell"><svg class="icon"><use href="#tick"/></svg></div><div class="cell"><svg class="icon"><use href="#tick"/></svg></div></div>
    <div class="row"><div class="label">24x7 Security Operations Centre (SOC) - Monitoring Cloud Office</div><div class="cell"><svg class="icon"><use href="#tick"/></svg></div><div class="cell"><svg class="icon"><use href="#tick"/></svg></div></div>
    <div class="row"><div class="label">Dark Web Scanning</div><div class="cell"><svg class="icon"><use href="#tick"/></svg></div><div class="cell"><svg class="icon"><use href="#tick"/></svg></div></div>
    <div class="row"><div class="label">Cloud Email Filtering</div><div class="cell"><svg class="icon"><use href="#tick"/></svg></div><div class="cell"><svg class="icon"><use href="#tick"/></svg></div></div>
    <div class="row"><div class="label">Cloud Office Backup</div><div class="cell"><svg class="icon"><use href="#tick"/></svg></div><div class="cell"><svg class="icon"><use href="#tick"/></svg></div></div>
    <div class="row"><div class="label">Automated Email Signatures</div><div class="cell"><svg class="icon"><use href="#tick"/></svg></div><div class="cell"><svg class="icon"><use href="#tick"/></svg></div></div>
    <div class="row"><div class="label">Endpoint Protection with EDR - Workstations &amp; Servers</div><div class="cell"><svg class="icon"><use href="#tick"/></svg></div><div class="cell"><svg class="icon"><use href="#tick"/></svg></div></div>
    <div class="row"><div class="label">3rd Party Applications Updating</div><div class="cell"><svg class="icon"><use href="#cross"/></svg></div><div class="cell"><svg class="icon"><use href="#tick"/></svg></div></div>
    <div class="row"><div class="label">24x7 Security Operations Centre (SOC) -<small>Monitoring Endpoints and Servers</small></div><div class="cell"><svg class="icon"><use href="#cross"/></svg></div><div class="cell"><svg class="icon"><use href="#tick"/></svg></div></div>
    <div class="row"><div class="label">Privileged Access Management &amp; Application Whitelisting</div><div class="cell"><svg class="icon"><use href="#cross"/></svg></div><div class="cell"><svg class="icon"><use href="#tick"/></svg></div></div>
    <div class="row"><div class="label">Internal Vulnerability Scanning</div><div class="cell"><svg class="icon"><use href="#cross"/></svg></div><div class="cell"><svg class="icon"><use href="#tick"/></svg></div></div>
    <div class="row row--tall"><div class="label">Backup &amp; Disaster Recovery to comply with<small>ACSC Essential 8 Maturity Level 1</small></div><div class="cell"><svg class="icon"><use href="#cross"/></svg></div><div class="cell">Pending<br>Assessment</div></div>

    <div class="price-block">
      <div class="price-line"><span class="name">RRP / User</span><span class="val">$110</span><span class="val">$35</span><span class="val">$60</span></div>
      <div class="price-line"><span class="name">Minimum User Count</span><span class="val">5</span><span class="val">5</span><span class="val">5</span></div>
      <div class="price-line"><span class="name">Minimum Monthly Commit</span><span class="val">$550</span><span class="val">$175</span><span class="val">$300</span></div>
    </div>
  </div>

  <div class="brand">
    <span class="dot"></span>
    <span class="name">NORTHGATE</span>
  </div>

  <footer class="footer">
    <p class="company">NORTHGATE COMPUTER SERVICES PTY LTD | ABN: 51 208 334 917</p>
    <p class="contact">northgatecomputers.com.au | service@northgatecomputers.com.au<br>12/48 Ashby Rd, Riverside Park, VIC, 3099 | 1300 555 019</p>
  </footer>
</section>
</body>
</html>
```